Refresh of The Marston Collective business card

Update business card design using existing primary logo. Names, numbers, etc. are too hard to read on current design.

Target Market(s)

We are a CPA firm.

Industry/Entity Type

Accountant

Contact Information for Business Card

update current card

Colors
0355a3
3176b5
85acd3
0792cd

Requirements
Must have
• Easier to read phone numbers and names
• Use existing logo
Nice to have
• We love our color scheme and current TMC logo. But the names and phone numbers are too small and card just look old and stale.

```html
<!DOCTYPE html>
<html lang="en">
<head>
<meta charset="utf-8">
<title>The Marston Collective — Business Card</title>
<link rel="stylesheet" href="https://fonts.googleapis.com/css2?family=Tinos:wght@400;700&family=Source+Sans+3:wght@400;600&display=swap">
<style>
  :root {
    --backdrop: #232323;
    --navy: #0b3878;
    --primary: #0355a3;
    --mid: #3176b5;
    --light: #85acd3;
    --ink: #2a2a2a;
    --rule: #555555;
    --white: #ffffff;
  }
  * { margin: 0; padding: 0; box-sizing: border-box; }
  html, body { width: 1200px; height: 900px; overflow: hidden; }
  body { background: var(--backdrop); position: relative; font-family: "Source Sans 3", Arial, sans-serif; }

  .card { position: absolute; top: 170px; width: 347px; height: 561px; }
  .card-front { left: 259px; background: var(--white); text-align: center; }
  .card-back {
    left: 631px; overflow: hidden;
    background: radial-gradient(ellipse at 50% 38%, var(--mid) 0%, #1f5ea6 45%, #124a8e 100%);
  }

  /* front */
  .brand-circle {
    position: absolute; left: 73px; top: 59px; width: 200px; height: 200px;
    border-radius: 50%;
    background: radial-gradient(circle at 50% 30%, var(--mid), var(--primary) 60%, #063f80);
  }
  .brand-initials {
    position: absolute; left: 0; right: 0; top: 268px;
    font-family: "Tinos", "Times New Roman", serif; font-weight: 700;
    font-size: 15px; letter-spacing: 3px; color: var(--navy);
  }
  .person-name {
    position: absolute; left: 0; right: 0; top: 310px;
    font-family: "Tinos", "Times New Roman", serif; font-weight: 700;
    font-size: 21px; color: var(--navy); letter-spacing: 0.3px;
  }
  .name-rule { position: absolute; left: 107px; width: 133px; top: 354px; border-top: 1px solid var(--rule); }
  .contact-list { position: absolute; left: 0; right: 0; top: 376px; list-style: none; font-size: 17px; line-height: 23px; color: var(--ink); }
  .contact-list .label { font-weight: 600; color: var(--navy); }
  .address { position: absolute; left: 0; right: 0; top: 478px; font-size: 17px; line-height: 23px; color: var(--ink); }

  /* back */
  .sheen { position: absolute; inset: 0; }
  .back-mark { position: absolute; left: 33px; top: 223px; width: 94px; height: 94px; border-radius: 50%; background: var(--white); }
  .back-wordmark { position: absolute; left: 138px; top: 228px; width: 180px; color: var(--white); text-align: center; }
  .back-wordmark .wm-rule { border-top: 1px solid var(--white); }
  .back-wordmark .wm-name {
    font-family: "Tinos", "Times New Roman", serif; font-weight: 400;
    font-size: 19px; line-height: 24px; letter-spacing: 1.5px; text-transform: uppercase;
    padding: 6px 0;
  }
  .tagline { margin-top: 6px; font-size: 8px; font-weight: 600; letter-spacing: 1.6px; text-transform: uppercase; }
  .website { position: absolute; left: 0; right: 0; top: 484px; text-align: center; color: var(--white); font-size: 17px; }
</style>
</head>
<body>
  <section class="card card-front">
    <div class="brand-circle"></div>
    <div class="brand-initials">TMC</div>
    <h1 class="person-name">DANIEL R. MARSTON, CPA</h1>
    <div class="name-rule"></div>
    <ul class="contact-list">
      <li><span class="label">P:</span> 321.555.0148</li>
      <li><span class="label">M:</span> 321.555.0172</li>
      <li><span class="label">F:</span> 321.555.0190</li>
      <li><span class="label">E:</span> dan@marstoncollective.com</li>
    </ul>
    <p class="address">418 Lakeview Ave.Suite 112<br>Winter Park,Florida 32789</p>
  </section>

  <section class="card card-back">
    <svg class="sheen" width="347" height="561" viewBox="0 0 347 561" aria-hidden="true">
      <path d="M0 300 C120 250 250 170 347 60 L347 0 L0 0 Z" fill="#ffffff" opacity="0.05"/>
      <path d="M0 360 C140 330 260 250 347 150" fill="none" stroke="#ffffff" stroke-width="1" opacity="0.12"/>
    </svg>
    <div class="back-mark"></div>
    <div class="back-wordmark">
      <div class="wm-rule"></div>
      <div class="wm-name">The Marston<br>Collective</div>
      <div class="wm-rule"></div>
      <div class="tagline">Certified Public Accountants</div>
    </div>
    <p class="website">www.marstoncollective.com</p>
  </section>
</body>
</html>
```